Business Card Design

We are looking for a business card designed for our landscaping company. We do landscaping installation & Maintenance Services. We would like to see designs that have basic landscaping in background. We also think it is important to have both of our names and phone numbers on the card. We need something that stands out a little whether it is shape of the card or thickness or design.

Industry/Entity Type

Business

Contact Information for Business Card

Pale Ridge Yardworks, paleridgeyardworks@mailbrook.net, Dale Purvine 555-213-7690, Martin Kolbey 555-864-1037

```html
<!DOCTYPE html>
<html lang="en">
<head>
<meta charset="utf-8">
<title>Pale Ridge Yardworks — Business Card</title>
<link rel="stylesheet" href="https://fonts.googleapis.com/css2?family=Nunito+Sans:wght@400;600&display=swap">
<style>
  :root {
    --page-bg: #ecebe7;
    --card-bg: #f6f7f3;
    --scene-light: #f3f4ef;
    --scene-green: #e3e8dc;
    --scene-bloom: #efe6ea;
    --leaf-green: #5fae47;
    --deep-green: #4a9a3a;
    --earth-brown: #a9875d;
    --bark-brown: #6b4e35;
    --ink-dark: #333333;
    --white: #ffffff;
  }
  * { margin: 0; padding: 0; box-sizing: border-box; }
  html, body {
    width: 1200px; height: 1000px; overflow: hidden;
    background: var(--page-bg);
    font-family: "Nunito Sans", Arial, sans-serif;
  }
  .business-card {
    position: absolute; left: 150px; top: 231px;
    width: 900px; height: 538px;
    background: var(--card-bg);
    overflow: hidden;
    box-shadow: 0 10px 30px rgba(0,0,0,0.18);
  }
  .garden-backdrop {
    position: absolute; inset: 0;
    background:
      radial-gradient(ellipse at 85% 65%, var(--scene-bloom) 0%, transparent 40%),
      radial-gradient(ellipse at 10% 40%, var(--scene-green) 0%, transparent 45%),
      linear-gradient(180deg, var(--scene-green) 0%, var(--scene-light) 45%, var(--scene-light) 100%);
  }
  .brand-name {
    position: absolute; right: 44px; top: 62px;
    display: flex; align-items: center; gap: 14px;
    font-size: 46px; font-weight: 600; color: var(--deep-green);
    letter-spacing: 0.5px; white-space: nowrap;
  }
  .brand-dot {
    width: 22px; height: 22px; border-radius: 50%;
    background: var(--leaf-green);
  }
  .contacts {
    position: absolute; left: 45px; top: 238px;
  }
  .contact-name {
    font-size: 32px; font-weight: 400; color: var(--leaf-green);
    line-height: 1.2;
  }
  .contact-phone {
    display: flex; align-items: center; gap: 7px;
    font-size: 21px; color: var(--ink-dark); line-height: 1.3;
    margin-bottom: 18px;
  }
  .contact-phone svg { width: 18px; height: 18px; }
  .contact-email {
    font-size: 22px; color: var(--leaf-green); margin-top: 4px;
  }
  .wave-band {
    position: absolute; left: 0; bottom: 0; width: 900px; height: 538px;
  }
</style>
</head>
<body>
  <div class="business-card">
    <div class="garden-backdrop" role="img" aria-label="Faded photo of a landscaped front yard with lawn, flower beds and a house porch"></div>

    <div class="brand-name"><span class="brand-dot"></span>Pale Ridge Yardworks</div>

    <div class="contacts">
      <div class="contact-name">Dale Purvine</div>
      <div class="contact-phone">
        <svg viewBox="0 0 24 24" aria-hidden="true"><path fill="#333" d="M6.6 10.8a15.1 15.1 0 0 0 6.6 6.6l2.2-2.2a1 1 0 0 1 1-.25 11.4 11.4 0 0 0 3.6.57 1 1 0 0 1 1 1V20a1 1 0 0 1-1 1A17 17 0 0 1 3 4a1 1 0 0 1 1-1h3.5a1 1 0 0 1 1 1c0 1.25.2 2.45.57 3.6a1 1 0 0 1-.25 1z"/></svg>
        555-213-7690
      </div>
      <div class="contact-name">Martin Kolbey</div>
      <div class="contact-phone">
        <svg viewBox="0 0 24 24" aria-hidden="true"><path fill="#333" d="M6.6 10.8a15.1 15.1 0 0 0 6.6 6.6l2.2-2.2a1 1 0 0 1 1-.25 11.4 11.4 0 0 0 3.6.57 1 1 0 0 1 1 1V20a1 1 0 0 1-1 1A17 17 0 0 1 3 4a1 1 0 0 1 1-1h3.5a1 1 0 0 1 1 1c0 1.25.2 2.45.57 3.6a1 1 0 0 1-.25 1z"/></svg>
        555-864-1037
      </div>
      <div class="contact-email">paleridgeyardworks@mailbrook.net</div>
    </div>

    <svg class="wave-band" viewBox="0 0 900 538" aria-hidden="true">
      <defs>
        <linearGradient id="brownBand" x1="0" x2="1" y1="0" y2="0">
          <stop offset="0" stop-color="var(--bark-brown)"/>
          <stop offset="1" stop-color="var(--earth-brown)"/>
        </linearGradient>
      </defs>
      <path fill="url(#brownBand)" d="M0,448 C150,470 300,482 450,466 C600,448 760,402 900,404 L900,430 C760,430 610,468 450,486 C300,502 150,496 0,482 Z"/>
      <path fill="var(--white)" d="M0,478 C150,494 300,500 450,484 C610,466 760,428 900,426 L900,436 C760,440 610,476 450,494 C300,510 150,506 0,490 Z"/>
      <path fill="var(--leaf-green)" d="M0,488 C150,504 300,508 450,492 C610,474 760,438 900,434 L900,538 L0,538 Z"/>
    </svg>
  </div>
</body>
</html>
```